Website design for Cambridge based systematic hedge fund

We have run previous craftmosaic competitions to design our company logo, business cards and the styling of our presentation deck (see attached files).
As the final step we are looking to get a website designed that is thematically consistent with these existing elements of our branding.
You can find some of our competitors websites below:
https://www.quelmarsh.example/
https://www.fenloor.example/
https://www.pyvart.example/
https://www.dulvet.example/
https://www.orbelmfunds.example/
https://www.valtrigo.example/
https://www.meskilfunds.example/home
We would like to have a website that works well on both mobile devices and desktops. Either just as one page that can be scrolled down, with links at the top that skips to certain sections, or a few separate pages that can be navigated by a top menu.
It should look professional, we are not after lots of animations or unnecessary transitions, and in particular the website must be smooth to navigate. We would like to avoid having peoples of people, we are happy to make use of elements from the presentation (for example the style of the cover slide, or the section slides with the faded bridge in the background), or 'financial' style images.
We would like to have the following sections for now. For some of these some example text has been provided, final text may change but it will be of similar length. For the other sections we are happy to just have template text for now. At the moment we are mainly interested to see styles/layouts as words can be added easily afterwards:
1) We will need a disclaimer pop up the first time someone visits the site (see for example the meskilfunds example).
2) Top page - company name, then in larger text "Bringing AI and Statistical Inference to Financial Markets", and somewhere in smaller text "Harlow Vectors is a quantitative asset manager with the singular focus of delivering algorithmic strategies that work"
3) "About us" section: will describe us as a company, details our approach, company values, and explains the company logo.
Example text:
"We deliver consistent alpha across liquid markets through the application of proprietary IP in Bayesian inference, machine learning and artificial intelligence. We are a multi-disciplinary team founded by experienced finance professionals from premier institutions, leading academics from the Thornbury Stellar Unit at Ashmere College and world-class software engineers.
Our logo portrays a sillhoute of the lattice walkway at Ashmere College. Our unique scientific approach allows us to bridge cutting-edge mathematical research and computing expertise with financial knowledge to bring algorithmns that work to liquid markets"
4) Hiring section, detailing our culture, what we are looking for.
Example text:
"We are always looking for exceptional talent to join our entrepreneurial team. We are looking for individuals who are creative thinkers, can demonstrate analytical rigour and are passionate about the intersection of science, finance and technology.
We prioritise having a company culture that promotes sharing ideas in a safe, collaborative research environment. We make sure that every member of the team has the oppertunity to explore their own ideas through weekly 'innovation time', and ensure that everyone gets the support they need to continue to grow as individuals within the company."
5) A section for news/press releases
6) Contact us area at the bottom with office location and email. We will need to list 3 addresses for our Cambridge, London and Singapore offices, along with a couple of contact emails or phone numbers
7) A client login button at the top that will take them to a different website (unrelated to this one).

```html
<!DOCTYPE html>
<html lang="en">
<head>
<meta charset="utf-8">
<title>Harlow Vectors</title>
<link rel="stylesheet" href="https://fonts.googleapis.com/css2?family=Montserrat:wght@600;700&family=Roboto:wght@400;500;700&display=swap">
<style>
  :root {
    --sky: #5b9bd9;
    --navy: #02446f;
    --ink-blue: #0b4473;
    --pale: #bcd6ef;
    --card: #cccccc;
    --card-edge: #4a86c8;
    --soft-grey: #d9d9d9;
    --dark-text: #26303c;
    --black: #111111;
    --white: #ffffff;
  }
  * { margin: 0; padding: 0; box-sizing: border-box; }
  html, body { width: 1200px; height: 3742px; overflow: hidden; }
  body { position: relative; font-family: "Roboto", Arial, sans-serif; background: var(--sky); }
  .abs { position: absolute; }
  .heading { font-family: "Montserrat", Arial, sans-serif; font-weight: 700; }

  /* header */
  .site-header { left: 0; top: 0; width: 1200px; height: 99px; background: var(--sky); }
  .brand { display: flex; align-items: center; gap: 8px; font-family: "Montserrat", Arial, sans-serif; font-weight: 700; font-size: 19px; color: var(--black); letter-spacing: 0.5px; }
  .brand-mark { width: 14px; height: 14px; background: var(--black); }
  .site-header .brand { left: 142px; top: 38px; }
  .main-nav a { position: absolute; top: 47px; font-size: 14px; font-weight: 700; color: var(--black); text-decoration: none; white-space: nowrap; }
  .main-nav a.current { color: var(--ink-blue); }
  .main-nav a.current::after { content: ""; position: absolute; left: 0; top: 25px; width: 18px; height: 3px; background: var(--ink-blue); }
  .login-btn { left: 972px; top: 41px; width: 85px; height: 31px; border: 2px solid var(--navy); border-radius: 7px; color: var(--navy); font-size: 14px; font-weight: 700; display: flex; align-items: center; justify-content: center; }

  /* hero */
  .hero { left: 0; top: 99px; width: 1200px; height: 652px; background: var(--navy); overflow: hidden; }
  .hero-network { right: 0; top: 0; width: 860px; height: 652px; background: radial-gradient(ellipse at 85% 45%, rgba(200,200,200,0.28), rgba(2,68,111,0) 65%); }
  .hero-title { left: 140px; top: 70px; font-size: 52px; color: var(--sky); letter-spacing: 0.5px; }
  .hero-tagline { left: 140px; top: 156px; width: 620px; font-size: 40px; line-height: 49px; color: var(--soft-grey); font-weight: 600; }
  .hero-intro { left: 140px; top: 335px; width: 500px; font-size: 22px; line-height: 37px; color: #222c38; font-weight: 500; }

  /* section title underline */
  .rule { height: 5px; width: 37px; border-radius: 3px; }

  /* about */
  .about { left: 0; top: 751px; width: 1200px; height: 709px; background: var(--sky); }
  .about-visual { left: 0; top: 190px; width: 555px; height: 295px; background: linear-gradient(160deg, rgba(188,214,239,0.8), rgba(2,68,111,0.55)); border-radius: 0 120px 0 0; }
  .about-title { left: 620px; top: 40px; font-size: 40px; color: var(--soft-grey); }
  .about .rule { left: 620px; top: 95px; background: var(--soft-grey); }
  .about-text { left: 616px; top: 127px; width: 445px; font-size: 22px; line-height: 27.5px; font-weight: 700; color: var(--dark-text); }
  .about-text p + p { margin-top: 27px; }

  /* hiring */
  .hiring { left: 0; top: 1460px; width: 1200px; height: 712px; background: var(--pale); }
  .hiring-title { left: 141px; top: 38px; font-size: 43px; color: var(--ink-blue); }
  .hiring .rule { left: 141px; top: 95px; background: var(--ink-blue); }
  .hiring-text { left: 141px; top: 148px; width: 540px; font-size: 22px; line-height: 27.5px; font-weight: 700; color: var(--black); }
  .hiring-text p + p { margin-top: 27px; }
  .more-btn { left: 141px; top: 599px; width: 110px; height: 33px; background: var(--ink-blue); border-radius: 6px; color: var(--white); font-size: 13px; font-weight: 700; display: flex; align-items: center; justify-content: center; }
  .culture-visual { left: 654px; top: 116px; width: 406px; height: 452px; border-radius: 50%; background: radial-gradient(circle at 40% 50%, rgba(91,155,217,0.35), rgba(188,214,239,0) 70%); }

  /* news */
  .news { left: 0; top: 2172px; width: 1200px; height: 707px; background: var(--navy); }
  .news-title { left: 0; top: 36px; width: 1200px; text-align: center; font-size: 40px; color: var(--sky); }
  .news .rule { left: 380px; top: 92px; background: var(--sky); }
  .news-card { top: 176px; width: 282px; height: 456px; background: var(--card); border: 2px solid var(--card-edge); padding: 26px 16px 0 17px; }
  .news-card h3 { font-size: 19px; line-height: 23px; font-weight: 700; color: var(--ink-blue); }
  .news-card p { margin-top: 26px; font-size: 19.5px; line-height: 23.3px; color: var(--black); }
  .news-card .read-more { display: block; margin-top: 15px; font-size: 19.5px; color: var(--ink-blue); }

  /* contact */
  .contact { left: 0; top: 2879px; width: 1200px; height: 709px; background: var(--sky); }
  .contact-title { left: 0; top: 38px; width: 1200px; text-align: center; font-size: 40px; color: var(--ink-blue); }
  .contact .rule { left: 484px; top: 94px; background: var(--ink-blue); }
  .office-card { top: 162px; width: 282px; height: 456px; background: var(--card); border: 2px solid var(--ink-blue); }
  .office-card h3 { position: absolute; left: 13px; top: 27px; font-size: 19px; font-weight: 700; color: var(--ink-blue); }
  .office-map { position: absolute; left: 0; top: 78px; width: 278px; height: 167px; background: linear-gradient(135deg, #cfe3c8, #e9e3cf 55%, #aecdea); }
  .office-card .label { position: absolute; left: 13px; font-size: 14px; color: var(--ink-blue); }
  .office-card .line { position: absolute; left: 22px; font-size: 11.5px; color: var(--black); }

  /* footer */
  .site-footer { left: 0; top: 3588px; width: 1200px; height: 154px; background: var(--navy); }
  .site-footer .brand { left: 142px; top: 54px; }
  .footer-nav a { position: absolute; top: 47px; font-size: 13px; font-weight: 700; color: var(--black); text-decoration: none; white-space: nowrap; }
  .copyright { left: 0; top: 92px; width: 1346px; text-align: center; font-size: 13px; font-weight: 700; color: var(--white); }
</style>
</head>
<body>

<header class="site-header abs">
  <div class="brand abs"><span class="brand-mark"></span>HARLOW VECTORS</div>
  <nav class="main-nav">
    <a class="current" style="left:437px">HOME</a>
    <a style="left:528px">ABOUT US</a>
    <a style="left:648px">HIRING</a>
    <a style="left:747px">NEWS</a>
    <a style="left:837px">CONTACT US</a>
  </nav>
  <div class="login-btn abs">LOGIN</div>
</header>

<section class="hero abs">
  <div class="hero-network abs" role="img" aria-label="Network of connected nodes in pale grey"></div>
  <h1 class="hero-title heading abs">HARLOW VECTORS</h1>
  <h2 class="hero-tagline heading abs">Bringing AI And Statistical Inference To Financial Markets</h2>
  <p class="hero-intro abs">Harlow Vectors is a quantitative asset manager with the singular focus of delivering algorithmic strategies that work.</p>
</section>

<section class="about abs">
  <div class="about-visual abs" role="img" aria-label="Lattice walkway silhouette with connected node truss"></div>
  <h2 class="about-title heading abs">About Us</h2>
  <div class="rule abs"></div>
  <div class="about-text abs">
    <p>We deliver consistent alpha across liquid markets through the application of proprietary IP in Bayesian inference, machine learning and artificial intelligence. We are a multi-disciplinary team founded by experienced finance professionals from premier institutions, leading academics from the Thornbury Stellar Unit at Ashmere College and world-class software engineers.</p>
    <p>Our logo portrays a sillhoute of the lattice walkway at Ashmere College. Our unique scientific approach allows us to bridge cutting-edge mathematical research and computing expertise with financial knowledge to bring algorithmns that work to liquid markets</p>
  </div>
</section>

<section class="hiring abs">
  <h2 class="hiring-title heading abs">Hiring</h2>
  <div class="rule abs"></div>
  <div class="hiring-text abs">
    <p>We are always looking for exceptional talent to join our entrepreneurial team. We are looking for individuals who are creative thinkers, can demonstrate analytical rigour and are passionate about the intersection of science, finance and technology.</p>
    <p>We prioritise having a company culture that promotes sharing ideas in a safe, collaborative research environment. We make sure that every member of the team has the oppertunity to explore their own ideas through weekly 'innovation time', and ensure that everyone gets the support they need to continue to grow as individuals within the company.</p>
  </div>
  <div class="more-btn abs">MORE INFO</div>
  <div class="culture-visual abs" role="img" aria-label="Circular diagram of company values around the brand name"></div>
</section>

<section class="news abs">
  <h2 class="news-title heading abs">News / Press Release</h2>
  <div class="rule abs"></div>
  <article class="news-card abs" style="left:139px">
    <h3>Machine Learning In Cambridge</h3>
    <p>lorem ipsum dolor sit amet, consectetur adipiscing elit. nullam et tincidunt odio. cras libero turpis, efficitur ut scelerisque ut, dignissim quis quam. phasellus a purus sit amet sapien tempor vulputate quis iaculis neque. sed eget mi ligula. integer eleifend lacus et sapien.</p>
    <a class="read-more">read more</a>
  </article>
  <article class="news-card abs" style="left:458px">
    <h3>Artifical Intelligence In London</h3>
    <p>lorem ipsum dolor sit amet, consectetur adipiscing elit. nullam et tincidunt odio. cras libero turpis, efficitur ut scelerisque ut, dignissim quis quam. phasellus a purus sit amet sapien tempor vulputate quis iaculis neque. sed eget mi ligula. integer eleifend lacus et sapien.</p>
    <a class="read-more">read more</a>
  </article>
  <article class="news-card abs" style="left:777px">
    <h3>Construction Of Bridge In Singapore</h3>
    <p>lorem ipsum dolor sit amet, consectetur adipiscing elit. nullam et tincidunt odio. cras libero turpis, efficitur ut scelerisque ut, dignissim quis quam. phasellus a purus sit amet sapien tempor vulputate quis iaculis neque. sed eget mi ligula. integer eleifend lacus et sapien.</p>
    <a class="read-more">read more</a>
  </article>
</section>

<section class="contact abs">
  <h2 class="contact-title heading abs">Contact Us</h2>
  <div class="rule abs"></div>
  <div class="office-card abs" style="left:139px">
    <h3>Cambridge</h3>
    <div class="office-map" role="img" aria-label="Street map of Cambridge office area"></div>
    <span class="label" style="top:272px">Emails</span>
    <span class="line" style="top:301px">contact@harlowvectors.example</span>
    <span class="line" style="top:322px">info@harlowvectors.example</span>
    <span class="label" style="top:357px;left:10px">Phone Number</span>
    <span class="line" style="top:386px">+ 1223 500101</span>
    <span class="line" style="top:408px">+ 1223 500202</span>
  </div>
  <div class="office-card abs" style="left:458px">
    <h3>London</h3>
    <div class="office-map" role="img" aria-label="Street map of London office area"></div>
    <span class="label" style="top:272px">Emails</span>
    <span class="line" style="top:301px">contact@harlowvectors.example</span>
    <span class="line" style="top:322px">info@harlowvectors.example</span>
    <span class="label" style="top:357px;left:10px">Phone Number</span>
    <span class="line" style="top:386px">+ 020 7946 0311</span>
    <span class="line" style="top:408px">+ 020 7946 0422</span>
  </div>
  <div class="office-card abs" style="left:777px">
    <h3>Singapore</h3>
    <div class="office-map" role="img" aria-label="Street map of Singapore office area"></div>
    <span class="label" style="top:272px">Emails</span>
    <span class="line" style="top:301px">contact@harlowvectors.example</span>
    <span class="line" style="top:322px">info@harlowvectors.example</span>
    <span class="label" style="top:357px;left:10px">Phone Number</span>
    <span class="line" style="top:386px">+ 65 0065 0133</span>
    <span class="line" style="top:408px">+ 65 0065 0244</span>
  </div>
</section>

<footer class="site-footer abs">
  <div class="brand abs"><span class="brand-mark"></span>HARLOW VECTORS</div>
  <nav class="footer-nav">
    <a style="left:381px">HOME</a>
    <a style="left:472px">ABOUT US</a>
    <a style="left:593px">HIRING</a>
    <a style="left:692px">NEWS</a>
    <a style="left:782px">CONTACT US</a>
    <a style="left:921px">LOGIN</a>
  </nav>
  <p class="copyright abs">© 2021 HARLOW VECTORS</p>
</footer>

</body>
</html>
```